Refresh Application User Interface

Pellmark wishes to update the look of its business applications. Two representative forms are shown below. Please note, we are not considering changes in functionality or usability. Our goal is a cleaner, more contemporary design.

Industry/Entity Type

Business

```html
<!DOCTYPE html>
<html lang="en"><head><meta charset="utf-8"><title>Pellmark – Purchase Order</title>
<link href="https://fonts.googleapis.com/css2?family=Nunito+Sans:wght@400;600;700;800&display=swap" rel="stylesheet">
<style>
:root{--bar:#2e3137;--blue:#3a7bd5;--link:#2f6fc9;--muted:#8a9bb8;--text:#3b3f45;--line:#d9dde3;--band:#eef0f4;--green:#5cb85c;--red:#e0404a;--brand:#1d5fb6}
*{box-sizing:border-box;margin:0;padding:0}
html,body{width:836px;height:1200px;overflow:hidden;background:#fff;font-family:"Nunito Sans",sans-serif;color:var(--text)}
.stage{width:1044px;height:1500px;transform:scale(.8);transform-origin:0 0;position:relative}
.screen{position:absolute;left:0;width:1044px;height:749px}
.screen *{position:absolute}
.screen svg *,.screen b{position:static}
.topbar{left:0;top:0;width:1044px;height:46px;background:var(--bar);color:#fff;font-size:15px}
.topbar span{top:13px;white-space:nowrap}
.topbar b{font-weight:700}
.logout{color:#e85a5a}
.nav{top:68px;font-size:22px;color:#555;white-space:nowrap}
.nav.active{color:var(--blue);font-weight:700}
.sep{top:68px;font-size:22px;color:#999}
.brand{left:868px;top:66px;font-size:26px;font-weight:800;color:var(--brand);letter-spacing:1px}
.sub{top:118px;font-size:19px;color:var(--muted);white-space:nowrap}
.sub.on{color:#222}
.under{top:151px;height:4px;background:var(--blue)}
.rule{left:0;width:1044px;height:1px;background:var(--line)}
.title{left:23px;top:172px;font-size:22px;font-weight:400;color:#222}
.drop{left:482px;top:158px;width:130px;height:82px;background:#f3f4f6;font-size:11px;color:var(--muted)}
.drop span{left:10px}
.tabs{left:690px;top:181px;width:354px;height:23px;background:#e9ebef;font-size:11px}
.tabs span{top:4px}
.band{left:0;top:205px;width:1044px;height:37px;background:var(--band)}
.tool{top:10px;font-size:13px;color:var(--link);white-space:nowrap}
.tool.gray{color:#777}.tool.green{color:var(--green)}.tool.red{color:var(--red)}
.lbl{font-size:12.5px;color:#444;white-space:nowrap;text-align:right}
.hd{font-size:12.5px;color:#444;white-space:nowrap}
.in{height:24px;border:1px solid var(--line);border-radius:3px;background:#fff;font-size:11px;padding:5px 8px;white-space:nowrap;overflow:hidden}
.in.sel::after{content:"";position:absolute;right:6px;top:10px;border:4px solid transparent;border-top-color:#666}
.val{font-size:11px;white-space:nowrap}
.sec{top:482px;font-size:13px;color:var(--muted)}
.sec.on{color:#222}
.foot{left:0;top:705px;width:1044px;height:2px;background:var(--line)}
.msg{top:718px;font-size:17px;color:#8a9bb8}
.row-alt{left:0;width:1044px;background:#f6f7f9}
.ul{text-decoration:underline}
.chk{width:18px;height:18px;border:1px solid #bbb;border-radius:4px;background:#fff}
</style></head><body>
<div class="stage">

<!-- ===== Screen 1: shipping ===== -->
<section class="screen" style="top:0">
  <div class="topbar">
    <span style="left:13px">Logged In As <b>Dana Reyes</b> ⚙</span>
    <span style="left:217px">Current Role <b>administrator</b> ▾</span>
    <svg style="left:706px;top:10px" width="26" height="26" viewBox="0 0 26 26" fill="none" stroke="#fff" stroke-width="1.5"><path d="M9 14V5a2 2 0 0 1 4 0v7m0-2a2 2 0 0 1 4 0v3m0-1a2 2 0 0 1 4 0v5c0 4-3 6-6 6h-2c-3 0-5-2-7-6l-1-3a2 2 0 0 1 3-1l2 2"/></svg>
    <svg style="left:744px;top:12px" width="30" height="24" viewBox="0 0 30 24" fill="none" stroke="#fff" stroke-width="1.5"><rect x="2" y="2" width="20" height="14"/><rect x="5" y="6" width="20" height="14"/><circle cx="24" cy="19" r="4" fill="#5cb85c" stroke="none"/></svg>
    <span style="left:781px">New Tab</span>
    <svg style="left:857px;top:10px" width="26" height="26" viewBox="0 0 26 26" fill="none" stroke="#fff" stroke-width="1.5"><circle cx="13" cy="13" r="11"/><path d="M10 10a3 3 0 1 1 4 3v2"/><circle cx="13" cy="19" r=".8" fill="#fff"/></svg>
    <svg style="left:897px;top:10px" width="26" height="26" viewBox="0 0 26 26" fill="none" stroke="#fff" stroke-width="1.5"><path d="M4 15v-3a9 9 0 0 1 18 0v3"/><rect x="3" y="13" width="4" height="6" rx="2"/><rect x="19" y="13" width="4" height="6" rx="2"/><path d="M21 19c0 3-3 4-7 4"/></svg>
    <svg style="left:940px;top:10px" width="26" height="26" viewBox="0 0 26 26" fill="none" stroke="#e85a5a" stroke-width="1.5"><path d="M14 3H3v20h11M10 13h13m-4-4 4 4-4 4"/></svg>
    <span class="logout" style="left:973px">Log Out</span>
  </div>
  <span class="nav" style="left:23px">Home</span><span class="sep" style="left:102px">|</span>
  <span class="nav" style="left:130px">eSource</span><span class="sep" style="left:229px">|</span>
  <span class="nav active" style="left:257px">eBuy</span><span class="sep" style="left:328px">|</span>
  <span class="nav" style="left:355px">eRequest</span><span class="sep" style="left:466px">|</span>
  <span class="nav" style="left:494px">eStock</span><span class="sep" style="left:582px">|</span>
  <span class="nav" style="left:608px">ePlan</span><span class="sep" style="left:682px">|</span>
  <span class="nav" style="left:709px">Preferences</span>
  <span class="brand">PELLMARK</span>
  <span class="sub on" style="left:23px">Orders</span><span class="sub" style="left:103px">Receipts</span><span class="sub" style="left:197px">Shipments</span><span class="sub" style="left:308px">Invoices</span><span class="sub" style="left:400px">Pricing</span><span class="sub on" style="left:482px">Tables</span><span class="sub" style="left:558px">Reports</span><span class="sub" style="left:646px">Inquiries</span><span class="sub" style="left:742px">Periodic Tasks</span><span class="sub" style="left:882px">Workflows</span>
  <div class="under" style="left:24px;width:54px"></div><div class="under" style="left:482px;width:52px"></div>
  <div class="rule" style="top:156px"></div>
  <h1 class="title">Purchase Order</h1>
  <div class="band"></div>
  <div class="drop"><span style="top:6px">Inventroy Details</span><span style="top:28px">Stock Status</span><span style="top:60px">Product Sourcing</span></div>
  <div class="tabs"><span style="left:25px">Header</span><span style="left:108px;color:var(--green)">●</span><span style="left:129px">Lines</span><span style="left:202px">Changes</span><span style="left:278px;color:var(--green)">●</span><span style="left:299px">Notes</span></div>
  <span class="tool" style="left:17px;top:215px">▭ Post Order</span>
  <span class="tool gray" style="left:710px;top:215px">⌕ search</span><span class="tool gray" style="left:787px;top:215px">+ new</span><span class="tool" style="left:846px;top:215px">↶ back</span><span class="tool green" style="left:908px;top:215px">✓ apply</span><span class="tool red" style="left:974px;top:215px">✕ delete</span>

  <span class="lbl" style="left:0;width:74px;top:251px">Order #</span><span class="val" style="left:96px;top:253px">100159</span>
  <span class="lbl" style="left:0;width:74px;top:284px">Ship from</span>
  <div class="in" style="left:88px;top:279px;width:92px">1001</div><span class="val" style="left:188px;top:285px;color:var(--link)">/</span><div class="in" style="left:200px;top:279px;width:30px">0</div>
  <div class="in" style="left:88px;top:311px;width:244px;border-color:var(--blue)">Harbor Clinical Supply</div>
  <svg style="left:342px;top:313px" width="20" height="20" viewBox="0 0 20 20" fill="none" stroke="#3a7bd5" stroke-width="1.2"><circle cx="10" cy="10" r="8"/><ellipse cx="10" cy="10" rx="3.5" ry="8"/><path d="M2 10h16M3.5 6h13M3.5 14h13"/></svg>
  <span class="lbl" style="left:0;width:74px;top:346px">Address</span>
  <div class="in" style="left:88px;top:342px;width:244px">14 Quarry Rd</div>
  <div class="in" style="left:88px;top:374px;width:244px"></div>
  <span class="val" style="left:347px;top:378px;font-size:12px;color:var(--link)">DPV Unconfirmed</span>
  <span class="lbl" style="left:0;width:74px;top:410px">City</span><div class="in" style="left:88px;top:405px;width:178px">Millbrook</div>
  <span class="lbl" style="left:260px;width:49px;top:410px">State</span><div class="in" style="left:322px;top:405px;width:36px">MA</div>
  <svg style="left:368px;top:409px" width="16" height="16" viewBox="0 0 16 16" fill="none" stroke="#5cb85c" stroke-width="1.5"><rect x="1" y="1" width="14" height="14" rx="3"/><path d="M4 8l3 3 5-6"/></svg>
  <span class="val" style="left:388px;top:410px;font-size:12px;color:var(--green)">Accept</span>
  <span class="lbl" style="left:0;width:74px;top:442px">Zip</span><div class="in" style="left:88px;top:437px;width:100px">02340-1188</div>
  <span class="lbl" style="left:190px;width:56px;top:442px">Country</span><div class="in" style="left:258px;top:437px;width:102px">US</div>
  <span class="val ul" style="left:380px;top:442px;font-size:12px;color:var(--link)">Add Contact</span>

  <div style="left:0;top:472px;width:1044px;height:233px;background:#f9fafb"></div>
  <span class="sec" style="left:23px">Order Info</span><span class="sec on" style="left:109px">Shipping</span><span class="sec" style="left:186px">Payment</span><span class="sec" style="left:263px">Accounts</span><span class="sec" style="left:343px">Totals / Approval</span>
  <div style="left:109px;top:500px;width:52px;height:2px;background:var(--blue)"></div>

  <span class="lbl" style="left:0;width:115px;top:524px">Receive At</span><div class="in sel" style="left:124px;top:519px;width:132px">ALCH</div>
  <span class="lbl" style="left:0;width:115px;top:553px">Carrier</span><div class="in sel" style="left:124px;top:548px;width:132px">Northline</div>
  <span class="lbl" style="left:0;width:115px;top:582px">Express Service</span><div class="in sel" style="left:124px;top:577px;width:132px"></div>
  <span class="lbl" style="left:0;width:115px;top:612px">FOB</span><div class="in sel" style="left:124px;top:607px;width:132px"></div>
  <span class="lbl" style="left:0;width:115px;top:642px">Order Ship Rule</span><div class="in sel" style="left:124px;top:637px;width:168px">Partials</div>
  <span class="lbl" style="left:0;width:115px;top:671px">Line Ship Rule</span><div class="in sel" style="left:124px;top:666px;width:168px">Partials</div>
  <span class="lbl" style="left:270px;width:106px;top:524px">Request Date</span><div class="in" style="left:385px;top:519px;width:110px">01/07/2018</div>
  <svg style="left:498px;top:522px" width="16" height="17" viewBox="0 0 16 17" fill="none" stroke="#777"><rect x="1" y="3" width="14" height="13"/><path d="M1 7h14M5 1v4M11 1v4M4 10h2M7 10h2M10 10h2M4 13h2M7 13h2"/></svg>
  <span class="lbl" style="left:270px;width:106px;top:553px">Freight Terms</span><div class="in sel" style="left:385px;top:548px;width:132px">Collect</div>
  <span class="lbl" style="left:270px;width:106px;top:582px">Freight Calc</span><div class="in sel" style="left:385px;top:577px;width:168px"></div>
  <span class="lbl" style="left:540px;width:128px;top:524px">Customer Ship To</span><div class="in" style="left:682px;top:519px;width:92px"></div><span class="val" style="left:782px;top:524px;color:var(--link)">/</span><div class="in" style="left:794px;top:519px;width:30px"></div>
  <svg style="left:964px;top:638px" width="22" height="26" viewBox="0 0 22 26" fill="none" stroke="#3a7bd5" stroke-width="1.4"><path d="M6 11V7a5 5 0 0 1 10 0v4"/><rect x="2" y="11" width="18" height="13" rx="2"/><path d="M11 15v4"/></svg>

  <div class="foot"></div>
  <svg style="left:14px;top:716px" width="200" height="26" viewBox="0 0 200 26" fill="none" stroke="#3a7bd5" stroke-width="1.5"><path d="M4 15l9-9a4 4 0 0 1 6 6L9 22a3 3 0 0 1-4-4l9-9"/><path d="M40 2h10l5 5v17H40z M44 12h7M44 16h5"/><circle cx="52" cy="20" r="3"/><circle cx="80" cy="13" r="3" fill="#3a7bd5"/><circle cx="94" cy="5" r="3" fill="#3a7bd5"/><circle cx="94" cy="21" r="3" fill="#3a7bd5"/><path d="M80 13l14-8M80 13l14 8"/><rect x="121" y="6" width="24" height="18"/><path d="M128 6V2h10v4M121 13h24M130 13v4h6v-4"/><circle cx="180" cy="13" r="12"/><path d="M176 10a4 4 0 1 1 5 4v3"/></svg>
  <span class="msg" style="left:478px">Enter property values, and click Apply</span>
</section>

<!-- ===== Screen 2: lines ===== -->
<section class="screen" style="top:749px">
  <div class="topbar">
    <span style="left:13px">Logged In As <b>Dana Reyes</b> ⚙</span>
    <span style="left:217px">Current Role <b>administrator</b> ▾</span>
    <svg style="left:706px;top:10px" width="26" height="26" viewBox="0 0 26 26" fill="none" stroke="#fff" stroke-width="1.5"><path d="M9 14V5a2 2 0 0 1 4 0v7m0-2a2 2 0 0 1 4 0v3m0-1a2 2 0 0 1 4 0v5c0 4-3 6-6 6h-2c-3 0-5-2-7-6l-1-3a2 2 0 0 1 3-1l2 2"/></svg>
    <svg style="left:744px;top:12px" width="30" height="24" viewBox="0 0 30 24" fill="none" stroke="#fff" stroke-width="1.5"><rect x="2" y="2" width="20" height="14"/><rect x="5" y="6" width="20" height="14"/><circle cx="24" cy="19" r="4" fill="#5cb85c" stroke="none"/></svg>
    <span style="left:781px">New Tab</span>
    <svg style="left:857px;top:10px" width="26" height="26" viewBox="0 0 26 26" fill="none" stroke="#fff" stroke-width="1.5"><circle cx="13" cy="13" r="11"/><path d="M10 10a3 3 0 1 1 4 3v2"/><circle cx="13" cy="19" r=".8" fill="#fff"/></svg>
    <svg style="left:897px;top:10px" width="26" height="26" viewBox="0 0 26 26" fill="none" stroke="#fff" stroke-width="1.5"><path d="M4 15v-3a9 9 0 0 1 18 0v3"/><rect x="3" y="13" width="4" height="6" rx="2"/><rect x="19" y="13" width="4" height="6" rx="2"/><path d="M21 19c0 3-3 4-7 4"/></svg>
    <svg style="left:940px;top:10px" width="26" height="26" viewBox="0 0 26 26" fill="none" stroke="#e85a5a" stroke-width="1.5"><path d="M14 3H3v20h11M10 13h13m-4-4 4 4-4 4"/></svg>
    <span class="logout" style="left:973px">Log Out</span>
  </div>
  <span class="nav" style="left:23px">Home</span><span class="sep" style="left:102px">|</span>
  <span class="nav" style="left:130px">eSource</span><span class="sep" style="left:229px">|</span>
  <span class="nav active" style="left:257px">eBuy</span><span class="sep" style="left:328px">|</span>
  <span class="nav" style="left:355px">eRequest</span><span class="sep" style="left:466px">|</span>
  <span class="nav" style="left:494px">eStock</span><span class="sep" style="left:582px">|</span>
  <span class="nav" style="left:608px">ePlan</span><span class="sep" style="left:682px">|</span>
  <span class="nav" style="left:709px">Preferences</span>
  <span class="brand">PELLMARK</span>
  <span class="sub on" style="left:23px">Orders</span><span class="sub" style="left:103px">Receipts</span><span class="sub" style="left:197px">Shipments</span><span class="sub" style="left:308px">Invoices</span><span class="sub" style="left:400px">Pricing</span><span class="sub on" style="left:482px">Tables</span><span class="sub" style="left:558px">Reports</span><span class="sub" style="left:646px">Inquiries</span><span class="sub" style="left:742px">Periodic Tasks</span><span class="sub" style="left:882px">Workflows</span>
  <div class="under" style="left:24px;width:54px"></div><div class="under" style="left:482px;width:52px"></div>
  <div class="rule" style="top:156px"></div>
  <h1 class="title">Purchase Order</h1>
  <div class="band"></div>
  <div class="drop"><span style="top:6px">Inventroy Details</span><span style="top:28px">Stock Status</span><span style="top:60px">Product Sourcing</span></div>
  <div class="tabs"><span style="left:25px">Header</span><span style="left:89px;top:0;width:82px;height:23px;background:#dcdfe5"></span><span style="left:119px">Lines</span><span style="left:202px">Changes</span><span style="left:278px;color:var(--green)">●</span><span style="left:299px">Notes</span></div>
  <span class="tool" style="left:17px;top:215px">✂ View GL Accounts</span><span class="tool" style="left:161px;top:215px">▭ Post Order</span>
  <span class="tool gray" style="left:710px;top:215px">⌕ search</span><span class="tool gray" style="left:787px;top:215px">+ new</span><span class="tool" style="left:846px;top:215px">↶ back</span><span class="tool green" style="left:908px;top:215px">✓ apply</span><span class="tool red" style="left:974px;top:215px">✕ delete</span>

  <span class="lbl" style="left:0;width:74px;top:254px">Order #</span><span class="val" style="left:96px;top:257px">100159</span>
  <span class="val" style="left:196px;top:256px;font-size:12px;color:var(--green)">Regular Purchase Order</span>
  <span class="val" style="left:706px;top:256px;font-size:12px;color:var(--link)">Hold For Completion</span>
  <span class="val" style="left:196px;top:287px">Harbor Clinical Supply, Millbrook MA</span>

  <div style="left:0;top:318px;width:1044px;height:33px;background:#f3f4f6"></div>
  <span class="val" style="left:17px;top:321px;font-size:20px;font-weight:800;color:var(--link)">Σ</span>
  <svg style="left:45px;top:324px" width="110" height="20" viewBox="0 0 110 20" fill="none" stroke="#3a7bd5" stroke-width="1.4"><rect x="1" y="1" width="12" height="15"/><rect x="5" y="4" width="12" height="15" fill="#fff"/><rect x="30" y="3" width="13" height="16"/><path d="M33 3V1h7v2M33 8h7M33 12h7M33 16h5"/><path d="M60 2v16m-3-3 3 3 3-3M66 3h8M66 8h6M66 13h4"/></svg>
  <span class="val" style="left:131px;top:320px;font-size:20px;font-weight:700;color:var(--red)">✕</span>
  <svg style="left:840px;top:326px" width="42" height="16" viewBox="0 0 42 16" fill="none" stroke="#999" stroke-width="1.3"><path d="M2 2v12M12 2 4 8l8 6zM28 2l-8 6 8 6zM38 2l-8 6 8 6z"/></svg>
  <span class="val" style="left:902px;top:327px;font-size:12px">Page 1 of 1</span>
  <svg style="left:982px;top:326px" width="42" height="16" viewBox="0 0 42 16" fill="none" stroke="#999" stroke-width="1.3"><path d="M2 2l8 6-8 6zM12 2l8 6-8 6zM28 2l8 6-8 6zM40 2v12"/></svg>

  <span class="hd" style="left:77px;top:357px">Line #</span><span class="hd" style="left:147px;top:357px">Product</span><span class="hd" style="left:254px;top:357px">Supplier Part#</span><span class="hd" style="left:363px;top:357px">Open Qty</span><span class="hd" style="left:471px;top:357px">Unit</span><span class="hd" style="left:584px;top:357px">Unit Price</span><span class="hd" style="left:703px;top:357px">Extended</span><span class="hd" style="left:789px;top:357px">LI Type / Ship To</span>
  <div class="chk" style="left:1000px;top:355px"></div>

  <!-- line 1 -->
  <span class="val ul" style="left:83px;top:390px;font-size:13px;color:var(--link)">20</span>
  <div class="in" style="left:147px;top:385px;width:72px">P-1100</div>
  <svg style="left:226px;top:389px" width="16" height="16" viewBox="0 0 16 16" fill="none" stroke="#3a7bd5" stroke-width="2"><circle cx="6.5" cy="6.5" r="5"/><path d="M10 10l5 5"/></svg>
  <div class="chk" style="left:279px;top:388px"></div>
  <div class="in" style="left:365px;top:385px;width:72px">1</div>
  <div class="in sel" style="left:471px;top:385px;width:74px">EA</div>
  <div class="in" style="left:584px;top:385px;width:72px">$5.00</div>
  <span class="val ul" style="left:703px;top:389px;font-size:13px;color:var(--link)">$5.00</span>
  <div class="in sel" style="left:789px;top:385px;width:155px">Receive&amp;Pay</div>
  <div class="chk" style="left:1000px;top:388px"></div>
  <div class="in" style="left:147px;top:416px;width:509px">Polar Crest 454230 - Recycled Laser Paper 1 case(2,500 count)- 24lb, 90 bright</div>
  <span class="val" style="left:703px;top:420px;font-size:13px;font-style:italic;color:var(--link)">ALCH</span>
  <div class="in sel" style="left:789px;top:416px;width:155px"></div>
  <span class="lbl" style="left:140px;width:133px;top:448px">On Purchase Orders</span><span class="val ul" style="left:280px;top:447px;font-size:13px;color:var(--link)">170</span>
  <span class="lbl" style="left:330px;width:85px;top:448px">Availiable</span><span class="val" style="left:422px;top:447px;font-size:13px;color:var(--link)">0</span>
  <span class="val ul" style="left:584px;top:449px;font-size:12px;color:var(--red)">Over Budget</span>
  <span class="val" style="left:703px;top:449px;font-size:12px;color:var(--red)">Pending</span>
  <svg style="left:810px;top:446px" width="74" height="24" viewBox="0 0 74 24" fill="none" stroke="#3a7bd5" stroke-width="1.3"><path d="M1 1h11l5 5v17H1zM4 10h10M4 14h10M4 18h7"/><rect x="53" y="3" width="19" height="19"/><path d="M53 8h19M57 1v4M68 1v4M56 11h3M61 11h3M66 11h3M56 15h3M61 15h3M66 15h3M56 18h3M61 18h3"/></svg>

  <!-- line 2 -->
  <div class="row-alt" style="top:473px;height:93px"></div>
  <span class="val ul" style="left:83px;top:483px;font-size:13px;color:var(--link)">20</span>
  <div class="in" style="left:147px;top:478px;width:72px">P-1100</div>
  <svg style="left:226px;top:482px" width="16" height="16" viewBox="0 0 16 16" fill="none" stroke="#3a7bd5" stroke-width="2"><circle cx="6.5" cy="6.5" r="5"/><path d="M10 10l5 5"/></svg>
  <div class="chk" style="left:279px;top:481px"></div>
  <div class="in" style="left:365px;top:478px;width:72px">1</div>
  <div class="in sel" style="left:471px;top:478px;width:74px">EA</div>
  <div class="in" style="left:584px;top:478px;width:72px">$5.00</div>
  <span class="val ul" style="left:703px;top:482px;font-size:13px;color:var(--link)">$5.00</span>
  <div class="in sel" style="left:789px;top:478px;width:155px">Receive&amp;Pay</div>
  <div class="chk" style="left:1000px;top:481px"></div>
  <div class="in" style="left:147px;top:509px;width:509px">Polar Crest 454230 - Recycled Laser Paper 1 case(2,500 count)- 24lb, 90 bright</div>
  <span class="val" style="left:703px;top:513px;font-size:13px;font-style:italic;color:var(--link)">ALCH</span>
  <div class="in sel" style="left:789px;top:509px;width:155px"></div>
  <span class="lbl" style="left:140px;width:133px;top:541px">On Purchase Orders</span><span class="val ul" style="left:280px;top:540px;font-size:13px;color:var(--link)">170</span>
  <span class="lbl" style="left:330px;width:85px;top:541px">Availiable</span><span class="val" style="left:422px;top:540px;font-size:13px;color:var(--link)">0</span>
  <span class="val ul" style="left:584px;top:542px;font-size:12px;color:var(--red)">Over Budget</span>
  <span class="val" style="left:703px;top:542px;font-size:12px;color:var(--red)">Pending</span>
  <svg style="left:810px;top:539px" width="74" height="24" viewBox="0 0 74 24" fill="none" stroke="#3a7bd5" stroke-width="1.3"><path d="M1 1h11l5 5v17H1zM4 10h10M4 14h10M4 18h7"/><rect x="53" y="3" width="19" height="19"/><path d="M53 8h19M57 1v4M68 1v4M56 11h3M61 11h3M66 11h3M56 15h3M61 15h3M66 15h3M56 18h3M61 18h3"/></svg>

  <!-- new line -->
  <div class="in" style="left:78px;top:572px;width:46px"></div>
  <div class="in" style="left:147px;top:572px;width:72px"></div>
  <svg style="left:226px;top:576px" width="16" height="16" viewBox="0 0 16 16" fill="none" stroke="#3a7bd5" stroke-width="2"><circle cx="6.5" cy="6.5" r="5"/><path d="M10 10l5 5"/></svg>
  <div class="chk" style="left:279px;top:575px"></div>
  <div class="in" style="left:365px;top:572px;width:72px"></div>
  <div class="in sel" style="left:471px;top:572px;width:74px"></div>
  <div class="in" style="left:584px;top:572px;width:72px"></div>
  <div class="in sel" style="left:789px;top:572px;width:155px">Receive&amp;Pay</div>
  <div class="in" style="left:147px;top:603px;width:509px"></div>
  <div class="in" style="left:789px;top:603px;width:155px;background:#f3f4f6"></div>

  <div class="foot"></div>
  <svg style="left:14px;top:716px" width="200" height="26" viewBox="0 0 200 26" fill="none" stroke="#3a7bd5" stroke-width="1.5"><path d="M4 15l9-9a4 4 0 0 1 6 6L9 22a3 3 0 0 1-4-4l9-9"/><path d="M40 2h10l5 5v17H40z M44 12h7M44 16h5"/><circle cx="52" cy="20" r="3"/><circle cx="80" cy="13" r="3" fill="#3a7bd5"/><circle cx="94" cy="5" r="3" fill="#3a7bd5"/><circle cx="94" cy="21" r="3" fill="#3a7bd5"/><path d="M80 13l14-8M80 13l14 8"/><rect x="121" y="6" width="24" height="18"/><path d="M128 6V2h10v4M121 13h24M130 13v4h6v-4"/><circle cx="180" cy="13" r="12"/><path d="M176 10a4 4 0 1 1 5 4v3"/></svg>
  <span class="msg" style="left:423px">Click Search, or enter property values and click Apply</span>
</section>

</div>
</body></html>
```